Next-Gen B2B Sales Negotiation App - UI Design for iOS

Develop a user-friendly dark-mode interface for a B2B sales negotiation assistant app for a company called Quorvel. The UI will showcase a single screen with features like counterparty search, agenda selection, and email drafting. Design should reflect a functional iOS app with realistic placeholder data to create a genuine experience.

Precise task description in attachment.

Target Market(s)

B2B

Requirements
Must have
• Each UI picture should look like a screen capture of an iphone
Nice to have
• The UI designs need to show the navigation and the app in use

```html
<!DOCTYPE html>
<html lang="en">
<head>
<meta charset="utf-8">
<title>Quorvel – New Negotiation</title>
<link rel="stylesheet" href="https://fonts.googleapis.com/css2?family=Plus+Jakarta+Sans:wght@300;400;500;600&display=swap">
<style>
  :root{
    --stage:#ff3390;
    --screen:#0b0c33;
    --screen-top:#15103a;
    --band:#2e0c2e;
    --card:#1b1b47;
    --field:#1a1a44;
    --pink:#ff2d87;
    --text:#ffffff;
    --muted:#8d8db5;
    --line:#2a2a5a;
  }
  *{box-sizing:border-box;margin:0;padding:0}
  html,body{width:704px;height:1200px;overflow:hidden}
  body{background:var(--stage);font-family:"Plus Jakarta Sans",sans-serif;color:var(--text);position:relative}
  .screen{position:absolute;left:201px;top:11px;width:302px;height:1178px;border-radius:14px;overflow:hidden;
    background:linear-gradient(180deg,var(--screen-top) 0%,var(--screen) 30%,var(--screen) 100%)}
  .abs{position:absolute}
  .header-band{left:0;top:70px;width:302px;height:60px;
    background:radial-gradient(ellipse 160px 30px at 50% 50%,var(--band),transparent 100%)}
  .status-time{left:24px;top:13px;font-size:13px;font-weight:500}
  .status-icons{right:24px;top:15px}
  .back{left:12px;top:56px}
  .title{left:0;right:0;top:53px;text-align:center;font-size:17px;font-weight:500}
  .section{left:13px;font-size:12.5px;font-weight:500}
  .section-sub{left:13px;font-size:10px;color:var(--muted);font-weight:300}
  .row{left:14px;width:274px;height:63px;border-radius:4px;background:var(--card)}
  .row.selected{height:58px;background:transparent;border:2px solid var(--pink)}
  .row.plain{background:transparent}
  .row .name{position:absolute;left:50px;top:12px;font-size:13px;font-weight:500}
  .row .label{position:absolute;left:50px;top:33px;font-size:10.5px;color:var(--muted);font-weight:300}
  .row .chev{position:absolute;right:12px;top:50%;transform:translateY(-50%)}
  .row .ico{position:absolute;left:13px;top:14px}
  .badge{position:absolute;left:12px;top:12px;width:31px;height:31px;border-radius:6px;background:var(--pink);display:flex;align-items:center;justify-content:center}
  .divider{left:70px;width:204px;height:1px;background:var(--line)}
  .tab{width:70px;text-align:center;font-size:7.5px;color:var(--muted)}
  .tab.active{color:var(--pink)}
  .tab svg{display:block;margin:0 auto 2px}
  .field{left:18px;width:266px;border-radius:4px;background:var(--field);padding:8px 10px}
  .field .flabel{font-size:10px;color:var(--muted);font-weight:300}
  .field .fvalue{font-size:12px;font-weight:300;margin-top:7px;line-height:18px;color:#e6e6f2}
  .btn{left:14px;width:274px;height:38px;border-radius:19px;display:flex;align-items:center;justify-content:center;gap:7px;font-size:12.5px}
  .btn.primary{background:var(--pink)}
  .btn.secondary{background:var(--card)}
  .nav{width:80px;text-align:center;font-size:8px;color:var(--muted);top:1119px}
  .nav.active{color:var(--pink)}
  .nav svg{display:block;margin:0 auto 2px}
  .home-bar{left:105px;top:1169px;width:92px;height:3px;border-radius:2px;background:#8a8aa8}
</style>
</head>
<body>
<main class="screen">
  <div class="abs header-band" role="img" aria-label="Soft decorative header band"></div>

  <div class="abs status-time">12:30</div>
  <svg class="abs status-icons" width="62" height="10" viewBox="0 0 62 10">
    <rect x="0" y="1" width="20" height="8" rx="4" fill="#9a9ab8"/><circle cx="15" cy="5" r="4" fill="#fff"/>
    <path d="M27 2 Q32 -1 37 2 L32 8 Z" fill="#fff"/>
    <rect x="44" y="1" width="15" height="8" rx="3" fill="#fff"/><rect x="59.5" y="3.5" width="1.5" height="3" fill="#fff"/>
  </svg>

  <svg class="abs back" width="12" height="14" viewBox="0 0 12 14"><path d="M8 2 L3 7 L8 12" stroke="#fff" stroke-width="1.5" fill="none"/></svg>
  <h1 class="abs title">New Negotiation</h1>

  <div class="abs section" style="top:125px">Select Counterparty</div>

  <div class="abs row selected" style="top:161px">
    <div class="badge" style="left:11px;top:11px">
      <svg width="16" height="14" viewBox="0 0 16 14" fill="none" stroke="#3a0a2a" stroke-width="1.3"><circle cx="8" cy="5" r="2.3"/><path d="M4 12c0-2.2 1.8-3.5 4-3.5s4 1.3 4 3.5"/><circle cx="3" cy="5.5" r="1.6"/><circle cx="13" cy="5.5" r="1.6"/><path d="M0.8 11c0-1.5 1-2.3 2.2-2.3M15.2 11c0-1.5-1-2.3-2.2-2.3"/></svg>
    </div>
    <div class="name" style="left:55px;top:9px">Brantor Inc.</div>
    <div class="label" style="left:55px;top:30px">Company</div>
    <svg class="chev" width="8" height="12" viewBox="0 0 8 12"><path d="M2 2 L6 6 L2 10" stroke="#fff" stroke-width="1.4" fill="none"/></svg>
  </div>

  <div class="abs row plain" style="top:230px;height:58px">
    <div class="badge" style="left:13px;top:11px">
      <svg width="14" height="16" viewBox="0 0 14 16" fill="none" stroke="#3a0a2a" stroke-width="1.3"><rect x="2.5" y="1" width="10" height="14" rx="1.5"/><circle cx="7.5" cy="6.5" r="1.8"/><path d="M4.8 11.5c0-1.5 1.2-2.3 2.7-2.3s2.7.8 2.7 2.3M1 4h3M1 8h3M1 12h3"/></svg>
    </div>
    <svg class="abs" style="left:58px;top:14px" width="10" height="11" viewBox="0 0 10 11" fill="none" stroke="#9a9ab8" stroke-width="1"><circle cx="5" cy="3.2" r="2.2"/><path d="M1 10c0-2.2 1.8-3.3 4-3.3s4 1.1 4 3.3Z"/></svg>
    <div class="name" style="left:77px;top:9px">CEO</div>
    <div class="label" style="left:57px;top:30px">Contact Person</div>
    <svg class="chev" width="8" height="12" viewBox="0 0 8 12"><path d="M2 2 L6 6 L2 10" stroke="#fff" stroke-width="1.4" fill="none"/></svg>
  </div>
  <div class="abs divider" style="top:289px"></div>

  <div class="abs section" style="top:322px">Choose an agenda</div>
  <div class="abs section-sub" style="top:340px">What is the desired outcomes</div>

  <div class="abs row" style="top:372px">
    <svg class="ico" width="18" height="18" viewBox="0 0 18 18" fill="none" stroke="var(--pink)" stroke-width="1.4"><circle cx="9" cy="9" r="7.3"/><path d="M9 5v4.3h3"/></svg>
    <div class="name">60 mins</div><div class="label">Desired Duration</div>
    <svg class="chev" width="8" height="12" viewBox="0 0 8 12"><path d="M2 2 L6 6 L2 10" stroke="#fff" stroke-width="1.4" fill="none"/></svg>
  </div>
  <div class="abs row" style="top:448px">
    <svg class="ico" width="18" height="18" viewBox="0 0 18 18" fill="none" stroke="var(--pink)" stroke-width="1.4"><circle cx="9" cy="9" r="7.3"/><path d="M9 5v4.3h3"/></svg>
    <div class="name">04/25/2025</div><div class="label">When</div>
    <svg class="chev" width="8" height="12" viewBox="0 0 8 12"><path d="M2 2 L6 6 L2 10" stroke="#fff" stroke-width="1.4" fill="none"/></svg>
  </div>
  <div class="abs row" style="top:525px">
    <svg class="ico" width="18" height="18" viewBox="0 0 18 18" fill="none" stroke="var(--pink)" stroke-width="1.4" stroke-linejoin="round"><path d="M16.5 1.5 L1.5 7.5 L8 10 L10.5 16.5 Z M8 10 L16.5 1.5"/></svg>
    <div class="name">Online</div><div class="label">Location</div>
    <svg class="chev" width="8" height="12" viewBox="0 0 8 12"><path d="M2 2 L6 6 L2 10" stroke="#fff" stroke-width="1.4" fill="none"/></svg>
  </div>
  <div class="abs row" style="top:601px">
    <svg class="ico" width="18" height="18" viewBox="0 0 18 18" fill="none" stroke="var(--pink)" stroke-width="1.3"><path d="M6.5 2h5l-1.5 2.5M6.5 2 8 4.5"/><path d="M8 4.5h2C14 7 15.5 10 15 13c-.4 2.3-2.5 3.5-6 3.5S3.4 15.3 3 13c-.5-3 1-6 5-8.5Z"/><path d="M10.3 8.8c-.4-.6-1-.8-1.6-.8-.9 0-1.5.5-1.5 1.2 0 1.6 3.2.9 3.2 2.6 0 .7-.7 1.2-1.7 1.2-.7 0-1.3-.3-1.6-.8M8.8 7v1M8.8 13v1"/></svg>
    <div class="name">We can make you more money</div><div class="label">Selling Point</div>
    <svg class="chev" width="8" height="12" viewBox="0 0 8 12"><path d="M2 2 L6 6 L2 10" stroke="#fff" stroke-width="1.4" fill="none"/></svg>
  </div>

  <div class="abs section" style="top:700px">Contact options</div>

  <div class="abs tab active" style="left:15px;top:740px">
    <svg width="16" height="13" viewBox="0 0 16 13" fill="none" stroke="var(--pink)" stroke-width="1.2"><rect x="1" y="1" width="14" height="11" rx="1.5"/><path d="M1.5 2 L8 7.5 L14.5 2M1.5 11.5 L6 6.5M14.5 11.5 L10 6.5"/></svg>Emails
  </div>
  <div class="abs" style="left:38px;top:775px;width:24px;height:2px;background:var(--pink)"></div>
  <div class="abs tab" style="left:116px;top:740px">
    <svg width="16" height="14" viewBox="0 0 16 14" fill="none" stroke="#9a9ab8" stroke-width="1.1"><rect x="1" y="1" width="14" height="12" rx="2"/><path d="M1 4.5h14M4 7.5h1M7.5 7.5h1M11 7.5h1M4 10h1M7.5 10h1M11 10h1"/></svg>Netlink
  </div>
  <div class="abs tab" style="left:217px;top:740px">
    <svg width="13" height="15" viewBox="0 0 13 15" fill="none" stroke="#9a9ab8" stroke-width="1.1"><path d="M1 1.5h7l4 4v8H1Z M8 1.5v4h4M3.5 8h6M3.5 10.5h6"/></svg>Phone call
  </div>
  <div class="abs" style="left:0;top:779px;width:302px;height:1px;background:var(--line)"></div>

  <div class="abs field" style="top:797px;height:55px">
    <div class="flabel">To</div>
    <div class="fvalue">Brantor Inc's CEO</div>
  </div>
  <div class="abs field" style="top:862px;height:125px">
    <div class="flabel">Message</div>
    <div class="fvalue">Hi Marten. I am reaching out to you as I have a solution to save your money and time. I am kindly proposing a meeting for week 8, for instance on Monday 17 February. Best regards, Oskari</div>
  </div>

  <div class="abs btn primary" style="top:1020px">
    <svg width="16" height="16" viewBox="0 0 18 18" fill="none" stroke="#fff" stroke-width="1.4" stroke-linejoin="round"><path d="M16.5 1.5 L1.5 7.5 L8 10 L10.5 16.5 Z M8 10 L16.5 1.5"/></svg>Send Now
  </div>
  <div class="abs btn secondary" style="top:1065px">
    <svg width="16" height="16" viewBox="0 0 18 18" fill="none" stroke="#fff" stroke-width="1.4"><circle cx="9" cy="9" r="7.3"/><path d="M9 5v4.3h3"/></svg>Schedule
  </div>

  <nav>
    <div class="abs nav active" style="left:10px">
      <svg width="18" height="17" viewBox="0 0 18 17" fill="none" stroke="var(--pink)" stroke-width="1.4" stroke-linejoin="round"><path d="M2 7.5 L9 1.5 L16 7.5 V15.5 H11 V11 H7 V15.5 H2 Z"/></svg>Home
    </div>
    <div class="abs nav" style="left:111px">
      <svg width="18" height="17" viewBox="0 0 18 17" fill="none" stroke="#b0b0cc" stroke-width="1.3" stroke-linejoin="round"><path d="M1.5 1.5h15v10H7l-4 4v-4H1.5Z M5 5h8M5 8h5"/></svg>Messages
    </div>
    <div class="abs nav" style="left:212px">
      <svg width="18" height="18" viewBox="0 0 18 18" fill="none" stroke="#b0b0cc" stroke-width="1.3"><circle cx="9" cy="9" r="2.6"/><path d="M9 1.2l1.5 2.2 2.6-.6.6 2.6 2.2 1.5-1.4 2.1 1.4 2.1-2.2 1.5-.6 2.6-2.6-.6L9 16.8l-1.5-2.2-2.6.6-.6-2.6-2.2-1.5L3.5 9 2.1 6.9l2.2-1.5.6-2.6 2.6.6Z"/></svg>Settings
    </div>
  </nav>
  <div class="abs home-bar"></div>
</main>
</body>
</html>
```